Fitness competition business needs a card design

I need a professional business card design using my logo. The card will be horizontal with rounded edges.

Target Market(s)

Female fitness competitors

Industry/Entity Type

Fitness

Contact Information for Business Card

Rose-Lynn Darby
Owner
stagevarno.com
555.301.2187
info@stagevarno.com

Font styles to use
Serif

Colors

Designer to choose colors to be used in the design.

Requirements
Must have
• On the back please add the following:
• Figure
• Bikini
• Physique
• Fitness
Nice to have
• Looking for a very sleek design, contemporary and easy to read.
Should not have
• Should not be difficult to read or be too busy

```html
<!DOCTYPE html>
<html lang="en">
<head>
<meta charset="utf-8">
<title>Stagevarno – Business Card</title>
<link href="https://fonts.googleapis.com/css2?family=Roboto+Condensed:wght@700&family=Roboto:wght@400&display=swap" rel="stylesheet">
<style>
  :root {
    --page: #d8d4cf;
    --card: #eeede9;
    --red: #c3252b;
    --charcoal: #48494b;
    --muted: #55565a;
    --mark-tone: #dcdad6;
  }
  html, body {
    margin: 0;
    width: 1200px;
    height: 1054px;
    overflow: hidden;
    background: var(--page);
  }
  .card {
    position: absolute;
    left: 100px;
    top: 225px;
    width: 1000px;
    height: 605px;
    background: var(--card);
    border-radius: 22px;
    box-shadow: 0 6px 24px rgba(0,0,0,0.12);
    overflow: hidden;
    font-family: "Roboto", Arial, sans-serif;
  }
  .brand {
    position: absolute;
    left: 51px;
    top: 56px;
    margin: 0;
    font-family: "Roboto Condensed", "Arial Narrow", sans-serif;
    font-weight: 700;
    font-size: 66px;
    line-height: 1;
    letter-spacing: 1px;
    color: var(--red);
    text-transform: uppercase;
  }
  .brand-mark {
    position: absolute;
    left: 460px;
    top: 10px;
    width: 560px;
    height: 600px;
  }
  .person-name {
    position: absolute;
    left: 51px;
    top: 306px;
    margin: 0;
    font-family: "Roboto Condensed", "Arial Narrow", sans-serif;
    font-weight: 700;
    font-size: 38px;
    color: var(--red);
  }
  .person-role {
    position: absolute;
    left: 51px;
    top: 356px;
    margin: 0;
    font-size: 25px;
    color: var(--muted);
  }
  .contacts {
    position: absolute;
    left: 51px;
    top: 432px;
    margin: 0;
    padding: 0;
    list-style: none;
  }
  .contacts li {
    display: flex;
    align-items: center;
    height: 41px;
    font-size: 25px;
    color: var(--charcoal);
  }
  .contacts svg {
    width: 20px;
    height: 20px;
    margin-right: 30px;
    flex: none;
  }
  .accent { color: var(--red); }
</style>
</head>
<body>
  <div class="card">
    <h1 class="brand">Stagevarno</h1>

    <svg class="brand-mark" viewBox="0 0 560 600" aria-hidden="true">
      <circle cx="300" cy="300" r="210" fill="var(--mark-tone)"/>
    </svg>

    <h2 class="person-name">Rose-Lynn Darby</h2>
    <p class="person-role">Owner</p>

    <ul class="contacts">
      <li>
        <svg viewBox="0 0 20 20" aria-hidden="true">
          <circle cx="10" cy="10" r="9" fill="none" stroke="var(--red)" stroke-width="1.6"/>
          <path d="M6 8.2c0-1 .8-1.7 4-1.7s4 .7 4 1.7v.8h-2v-.9H8v.9H6z" fill="var(--red)"/>
          <rect x="6.5" y="10" width="7" height="4" rx=".8" fill="var(--red)"/>
        </svg>
        555.301.2187
      </li>
      <li>
        <svg viewBox="0 0 20 20" aria-hidden="true">
          <circle cx="10" cy="10" r="9" fill="none" stroke="var(--red)" stroke-width="1.6"/>
          <circle cx="10" cy="10" r="5" fill="none" stroke="var(--red)" stroke-width="1.2"/>
          <path d="M5 10h10M10 5c-2 2.7-2 7.3 0 10M10 5c2 2.7 2 7.3 0 10" fill="none" stroke="var(--red)" stroke-width="1"/>
        </svg>
        <span>www.<span class="accent">stagevarno</span>.com</span>
      </li>
      <li>
        <svg viewBox="0 0 20 20" aria-hidden="true">
          <circle cx="10" cy="10" r="9" fill="none" stroke="var(--red)" stroke-width="1.6"/>
          <rect x="5.5" y="6.8" width="9" height="6.4" rx=".6" fill="var(--red)"/>
          <path d="M5.8 7.2 10 10.6l4.2-3.4" fill="none" stroke="var(--card)" stroke-width="1"/>
        </svg>
        info@stagevarno.com
      </li>
    </ul>
  </div>
</body>
</html>
```